Modern Business Card for Industrial Company

We need business cards updated with modern fonts and make it look more technical, sharp and clean. The logo should not be changed, but we are looking for fresh solutions for how other information on the card is laid out in an interesting way. The company provides machinery and services to the ceramic industry and deals with cutting-edge technology. The design should reflect a technologically advanced and modern company that deals with the latest European technologies.

Font styles to use
Sans Serif

Requirements
Must have
• Modern fonts, technical look and feel

```html
<!DOCTYPE html>
<html lang="en">
<head>
<meta charset="utf-8">
<title>Tessaro Business Card</title>
<link rel="stylesheet" href="https://fonts.googleapis.com/css2?family=Open+Sans:wght@400;600;700&display=swap">
<style>
  :root {
    --stage: #2b2b2b;
    --brand-blue: #05528f;
    --paper: #ffffff;
    --accent-red: #b3222a;
    --ink-light: #ffffff;
  }
  * { margin: 0; padding: 0; box-sizing: border-box; }
  html, body {
    width: 1200px; height: 1015px; overflow: hidden;
    background: var(--stage);
    font-family: "Open Sans", Arial, sans-serif;
  }
  .canvas {
    position: relative; width: 1200px; height: 1015px;
    display: flex; flex-direction: column; align-items: center; justify-content: center; gap: 56px;
  }
  .card {
    position: relative; width: 620px; height: 354px; overflow: hidden;
    background: var(--brand-blue);
    box-shadow: 0 10px 30px rgba(0,0,0,.45);
  }
  .card-back { display: flex; align-items: center; justify-content: center; }
  .wordmark {
    font-weight: 700; letter-spacing: 6px; text-transform: uppercase; line-height: 1;
  }
  .card-back .wordmark { color: var(--ink-light); font-size: 64px; }

  .front-art { position: absolute; inset: 0; }
  .front-wordmark {
    position: absolute; left: 470px; top: 150px; transform: translate(-50%, -50%);
    color: var(--brand-blue); font-size: 40px;
  }
  .identity { position: absolute; left: 44px; top: 96px; color: var(--ink-light); }
  .identity .person-name { font-size: 19px; font-weight: 600; letter-spacing: 2px; }
  .identity .person-role { font-size: 12px; letter-spacing: 1.5px; margin-top: 2px; }
  .address {
    position: absolute; left: 44px; top: 206px; color: var(--ink-light);
    font-size: 12.5px; letter-spacing: 1px; line-height: 1.45; text-transform: uppercase;
  }
  .contacts {
    position: absolute; left: 44px; top: 262px; list-style: none; color: var(--ink-light);
    font-size: 12.5px; letter-spacing: 1px; line-height: 1.5; text-transform: uppercase;
  }
  .contacts li { display: flex; align-items: center; gap: 8px; }
  .contacts svg { width: 13px; height: 13px; flex: none; }
</style>
</head>
<body>
<main class="canvas">

  <section class="card card-back" aria-label="Card back">
    <span class="wordmark">Tessaro</span>
  </section>

  <section class="card card-front" aria-label="Card front">
    <svg class="front-art" viewBox="0 0 620 354" aria-hidden="true">
      <circle cx="470" cy="120" r="212" fill="var(--paper)"/>
      <path d="M 276 60 A 205 205 0 0 0 430 320" fill="none" stroke="var(--accent-red)" stroke-width="3"/>
    </svg>
    <span class="wordmark front-wordmark">Tessaro</span>

    <div class="identity">
      <p class="person-name">MARCO RINALDI</p>
      <p class="person-role">PRESIDENT</p>
    </div>

    <address class="address">
      418 Halden Way, Suite 200<br>
      Brookfield, GA 30120
    </address>

    <ul class="contacts">
      <li>
        <svg viewBox="0 0 24 24" fill="var(--ink-light)"><path d="M6.6 10.8a15.1 15.1 0 0 0 6.6 6.6l2.2-2.2a1 1 0 0 1 1-.25 11.4 11.4 0 0 0 3.6.57 1 1 0 0 1 1 1V20a1 1 0 0 1-1 1A17 17 0 0 1 3 4a1 1 0 0 1 1-1h3.5a1 1 0 0 1 1 1c0 1.25.2 2.45.57 3.57a1 1 0 0 1-.25 1z"/></svg>
        21 555-0184
      </li>
      <li>
        <svg viewBox="0 0 24 24" fill="var(--ink-light)"><path d="M2 5h20v14H2z M3 6l9 7 9-7" stroke="var(--brand-blue)" stroke-width="1.5"/></svg>
        mrinaldi@tessaro.com
      </li>
      <li>
        <svg viewBox="0 0 24 24" fill="none" stroke="var(--ink-light)" stroke-width="2"><circle cx="12" cy="12" r="10"/><path d="M2 12h20M12 2c3 3 3 17 0 20M12 2c-3 3-3 17 0 20"/></svg>
        www.tessaro.com
      </li>
    </ul>
  </section>

</main>
</body>
</html>
```